Tolvik cards

I want a simple business card that pops.
Logo on one side.
On side two i want.
"Are you thinking about a new building on your property, or renovating an existing structure? Contact".....
Owners Name: Gary Pellman
Owners Phone number: 555-209-4176
Address:4716 Copper Fern RD, Alder Ridge, PA 10384
Committed to Quality, Service, and Integrity

```html
<!DOCTYPE html>
<html lang="en">
<head>
<meta charset="utf-8">
<title>Tolvik Builders LLC – Business Cards</title>
<link rel="stylesheet" href="https://fonts.googleapis.com/css2?family=Arimo:wght@400;700&display=swap">
<style>
  :root {
    --backdrop: #2a2a2a;
    --card: #f1f0ee;
    --brown: #4a3427;
    --brown-dark: #3d2a1f;
    --gold: #a48d6f;
    --gold-light: #b9a385;
    --ink: #2e231c;
    --rule: #c9bba6;
  }
  * { box-sizing: border-box; margin: 0; padding: 0; }
  html, body {
    width: 1138px; height: 1200px; overflow: hidden;
    background: var(--backdrop);
    font-family: "Arimo", Arial, sans-serif;
  }
  .card {
    position: absolute;
    width: 376px; height: 620px;
    background: var(--card);
    border-radius: 16px;
    overflow: hidden;
    color: var(--brown);
  }
  .card--front { left: 186px; top: 304px; }
  .card--back { left: 608px; top: 304px; }

  /* front */
  .front__mark {
    position: absolute; left: 128px; top: 90px;
    width: 120px; height: 120px;
    background: var(--brown);
  }
  .front__name {
    position: absolute; left: 0; right: 0; top: 448px;
    text-align: center; font-weight: 700; color: var(--brown);
  }
  .front__company { font-size: 62px; line-height: 1; letter-spacing: -1px; }
  .front__suffix { font-size: 22px; letter-spacing: 7px; margin-top: 4px; padding-left: 7px; }
  .front__tagline {
    position: absolute; left: 0; right: 0; top: 576px;
    text-align: center; font-size: 15.5px; color: var(--ink);
  }

  /* back */
  .back__band {
    position: absolute; left: 0; top: 0; bottom: 0; width: 78px;
    background: linear-gradient(90deg, var(--brown-dark), #7a634b 55%, var(--gold));
    display: flex; align-items: center; justify-content: center;
  }
  .back__question {
    writing-mode: vertical-rl; transform: rotate(180deg);
    color: #f5efe6; font-weight: 700; font-size: 14.6px;
    letter-spacing: 1.3px; line-height: 1.55; text-transform: uppercase;
    white-space: nowrap;
  }
  .back__logo {
    position: absolute; left: 78px; right: 0; top: 30px;
    text-align: center; font-weight: 700; color: var(--brown);
  }
  .back__mark { width: 44px; height: 44px; background: var(--brown); margin: 0 auto 14px; }
  .back__company { font-size: 46px; line-height: 1; letter-spacing: -0.5px; }
  .back__suffix { font-size: 14px; letter-spacing: 2px; margin-top: 2px; }
  .back__details { position: absolute; left: 104px; top: 228px; right: 20px; }
  .back__owner { font-size: 22px; font-weight: 700; letter-spacing: 0.5px; color: var(--ink); }
  .back__owner span { color: var(--gold); }
  .back__phone { font-size: 15.5px; font-weight: 700; color: var(--ink); margin-top: 12px; }
  .back__address { font-size: 14.5px; color: var(--gold-light); line-height: 1.5; margin-top: 4px; }
  .back__rule { border: 0; border-top: 1px solid var(--rule); width: 206px; margin: 17px 0 17px; }
  .back__tagline { font-size: 15px; color: var(--ink); line-height: 1.35; }
</style>
</head>
<body>
  <section class="card card--front" aria-label="Card front">
    <div class="front__mark"></div>
    <div class="front__name">
      <div class="front__company">TOLVIK</div>
      <div class="front__suffix">BUILDERS LLC</div>
    </div>
    <p class="front__tagline">Committed to Quality, Service &amp; Integrity</p>
  </section>

  <section class="card card--back" aria-label="Card back">
    <div class="back__band">
      <p class="back__question">Are you thinking about a new building on your<br>property, or renovating an existing structure?</p>
    </div>
    <div class="back__logo">
      <div class="back__mark"></div>
      <div class="back__company">TOLVIK</div>
      <div class="back__suffix">BUILDERS LLC</div>
    </div>
    <div class="back__details">
      <p class="back__owner">GARY <span>PELLMAN</span></p>
      <p class="back__phone">Call: 555-209-4176</p>
      <p class="back__address">Add.: 4716 Copper Fern RD,<br>Alder Ridge, PA 10384</p>
      <hr class="back__rule">
      <p class="back__tagline">Committed to Quality,<br>Service &amp; Integrity</p>
    </div>
  </section>
</body>
</html>
```